Tallow Brook Website - Sell Outdoor product

We are a mom and pop company that just opened our website.

We need a fresh, professional, and nice looking website for our outdoor products. We sell hunting, camping, fishing, and hiking products/accessories to name a few. Some of these products are optics, gun safes, gun bi-pods and tripods, gun lights, hunting camera, tents, hearing protection, targets, fishing poles, and hiking backpacks to name a few.

Our current website is: http://www.tallowbrook.example . You'll see our logo on the website, and it is attached. We aren't married to this logo, so if the designer thinks they can modify it or even come up with a better design for the website, they are more than welcome to do so. We need someone with good images of their own (clip art and/or outdoor images) they can use if they need to for our website.

I also attached a idea I had in visio, but please don't think this is set in stone. It is just a very rough idea. You can also go to our zintaro site to see what we sell: www.zintaro.example/shops/q7xk402mdrvp3s . Right now we sell everything on Zintaro, but our website will just focus on outdoor product. So please make it an outdoor focused website. And you can be creative with some of the product category names. We also want to leave room for some parallel product in the future. Like garden tools, back yard furniture, and BBQs.

Our company also wants to include a deals section on the website. We will probably update it once a week or month. I have included what I did for a deal and accompanying images for it. Image is called Morvelki (And the main images are 01 and 02).

We also want to make sure the file is compatible with our current web-hosting company, https://www.shelvora.example. So I included a webpage layout zip folder. If you have any questions, please contact me.

This is for a PSD and HTML/CSS webpage. If you have any artwork or images that you own and want to use them for the webpage, please do so.

Target Market(s)

The hunter, outdoors person, camper, hiker, and etc.

Industry/Entity Type

It Company

Coding

Coded - Design and coding required

Number of Pages Required

3 page

Requirements
Must have
• The main page. PSD and HTML/CSS file.
• The category page. PSD and HTML/CSS file
• The product display page. PSD and HTML/CSS file
• Please also use some images that you have or from the sites below:
• You can get free stock images for 7 days (20 per day) from this site:
• https://www.pixelbarn.example/complimentary/KTRPLQX/?utm_source=KTRPLQFreeX&utm_medium=cpc&utm_campaign=KTRPLQFreeX&gclid=ZXPq8rTmwnB4DHuLoPeaWs2kTb
• Has 14 good sites:
• http://www.ventureledger.example/article/519372
• Here are the ones I like:
• https://clearpane.example/
• http://grandolim.example/
• http://www.sitewright.example/free/nature
• http://www.dustvault.example/archive
• http://tinyframes.example/
• http://olq.brvkmt.example/search/hiking
• http://fetchqovi.blogspin.example/
• http://roelvastor.example/post/584930271164/download
• http://openvaultlibrary.example/
• If there is a photographer listed on or next to the image, on the bottom lower corner of the image, please put the photographer's name.
Nice to have
• I would like to have an unsubscribe page. If the designer has any of their own images of the outdoor world, and they want to use them, please do. Just make the right graphic changes to make it look good.
Should not have
• Try and keep green color to a minimum.

```html
<!DOCTYPE html>
<html lang="en">
<head>
<meta charset="utf-8">
<title>Tallow Brook – Outdoor Gear</title>
<link href="https://fonts.googleapis.com/css2?family=Montserrat:wght@600;700;800&family=Open+Sans:wght@400;600&display=swap" rel="stylesheet">
<style>
  :root {
    --ink: #2b2b2b;
    --topbar: #2b2b2b;
    --footer: #262626;
    --amber: #f0b21c;
    --amber-dark: #c98d05;
    --button-text: #8a5a00;
    --nav-grey: #8a8a8a;
    --card-bg: #efefef;
    --rule: #dcdcdc;
    --footer-text: #b9b9b9;
    --white: #ffffff;
  }
  * { box-sizing: border-box; margin: 0; padding: 0; }
  html, body { width: 1032px; height: 1200px; overflow: hidden; }
  body { position: relative; background: var(--white); font-family: "Open Sans", Arial, sans-serif; color: var(--ink); }

  .topbar { position: absolute; left: 0; top: 0; width: 1032px; height: 50px; background: var(--topbar); }
  .newsletter { position: absolute; left: 86px; top: 14px; display: flex; align-items: center; gap: 9px; font-size: 10px; color: #d6d6d6; }
  .newsletter-field { display: flex; width: 145px; height: 23px; border: 1px solid #6a6a6a; border-radius: 2px; }
  .newsletter-input { flex: 1; padding-left: 8px; line-height: 21px; font-size: 8.5px; color: #8c8c8c; background: #2f2f2f; }
  .newsletter-button { width: 54px; line-height: 21px; text-align: center; font-size: 8.5px; color: var(--amber); background: #1f1f1f; }
  .account-links { position: absolute; right: 88px; top: 18px; display: flex; gap: 10px; font-size: 9.5px; color: #d0d0d0; align-items: center; }
  .account-links .sep { color: #666; }
  .account-links svg { vertical-align: -1px; margin-right: 3px; }

  .brand-band { position: absolute; left: 0; top: 50px; width: 1032px; height: 80px; background: linear-gradient(180deg, #f3b61e, #eeac15); }
  .brand { position: absolute; left: 50%; top: 50px; transform: translateX(-50%); display: flex; align-items: center; gap: 10px; height: 80px; }
  .brand-mark { width: 22px; height: 22px; background: var(--ink); }
  .brand-name { font-family: "Montserrat", Arial, sans-serif; font-weight: 800; font-size: 30px; letter-spacing: 1px; color: var(--ink); }

  .main-nav { position: absolute; top: 159px; left: 0; width: 1032px; font-family: "Montserrat", Arial, sans-serif; font-weight: 700; font-size: 12px; letter-spacing: 0.8px; color: var(--nav-grey); }
  .main-nav a { position: absolute; text-decoration: none; color: inherit; white-space: nowrap; }
  .main-nav a.active { color: var(--ink); }
  .nav-rule { position: absolute; left: 183px; top: 186px; width: 764px; height: 1px; background: var(--rule); }
  .nav-active-bar { position: absolute; left: 189px; top: 183px; width: 60px; height: 4px; background: var(--amber); }
  .side-rule { position: absolute; left: 183px; top: 186px; width: 1px; height: 829px; background: var(--rule); }

  .category-list { position: absolute; left: 35px; top: 0; list-style: none; font-family: "Montserrat", Arial, sans-serif; font-weight: 700; font-size: 10px; letter-spacing: 0.8px; color: var(--nav-grey); }
  .category-list li { position: absolute; white-space: nowrap; }
  .category-list li.active { color: var(--ink); }

  .product-card { position: absolute; width: 355px; height: 174px; background: var(--card-bg); }
  .product-photo { position: absolute; left: 7px; top: 8px; width: 155px; height: 158px; background: var(--white); }
  .product-photo .shape { position: absolute; left: 20px; top: 20px; right: 20px; bottom: 20px; border-radius: 40%; }
  .product-title { position: absolute; left: 184px; top: 24px; width: 160px; font-size: 11.5px; line-height: 16px; color: #3a3a3a; }
  .product-price { position: absolute; left: 184px; top: 72px; font-size: 13px; color: #2f2f2f; }
  .product-price s { margin-right: 8px; }
  .buy-button { position: absolute; left: 184px; top: 105px; width: 91px; height: 37px; background: var(--amber); color: var(--button-text); font-size: 13px; line-height: 37px; text-align: center; border-radius: 2px; }

  .pagination { position: absolute; top: 988px; left: 0; font-size: 8px; color: #555; }
  .pagination span { position: absolute; width: 20px; height: 20px; border: 1px solid #9a9a9a; line-height: 18px; text-align: center; }

  .site-footer { position: absolute; left: 0; top: 1038px; width: 1032px; height: 162px; background: var(--footer); text-align: center; }
  .footer-links { position: absolute; top: 29px; width: 100%; font-size: 11px; color: var(--footer-text); }
  .footer-links .sep { margin: 0 8px; color: #777; }
  .copyright { position: absolute; top: 54px; width: 100%; font-size: 10.5px; color: var(--footer-text); }
  .helpline { position: absolute; top: 79px; width: 100%; font-size: 11.5px; color: var(--amber); }
  .social { position: absolute; top: 108px; left: 459px; display: flex; gap: 6px; }
  .social span { width: 24px; height: 24px; border-radius: 50%; background: #4a4a4a; }
</style>
</head>
<body>
  <header class="topbar">
    <div class="newsletter">
      <span>Join Our Newsletter</span>
      <div class="newsletter-field"><span class="newsletter-input">Email ID</span><span class="newsletter-button">Subscribe</span></div>
    </div>
    <nav class="account-links">
      <span><svg width="8" height="8" viewBox="0 0 8 8"><circle cx="4" cy="2.3" r="2" fill="#d0d0d0"/><path d="M0 8c0-3 2-4 4-4s4 1 4 4z" fill="#d0d0d0"/></svg>My Account</span>
      <span class="sep">|</span>
      <span><svg width="7" height="9" viewBox="0 0 7 9"><rect x="0" y="4" width="7" height="5" fill="#d0d0d0"/><path d="M1.5 4V2.5a2 2 0 0 1 4 0" stroke="#d0d0d0" fill="none"/></svg>Login</span>
      <span class="sep">|</span>
      <span><svg width="10" height="9" viewBox="0 0 10 9"><path d="M0 1h2l1.5 5h5L10 2H3" stroke="#d0d0d0" fill="none"/><circle cx="4" cy="8" r="1" fill="#d0d0d0"/><circle cx="8" cy="8" r="1" fill="#d0d0d0"/></svg>Shopping Cart</span>
    </nav>
  </header>

  <div class="brand-band"></div>
  <div class="brand"><span class="brand-mark"></span><span class="brand-name">TALLOW BROOK</span></div>

  <nav class="main-nav">
    <a class="active" style="left:201px">HOME</a>
    <a style="left:276px">HUNTING ACCESSORIES</a>
    <a style="left:462px">CAMPING</a>
    <a style="left:560px">FISHING</a>
    <a style="left:642px">HIKING</a>
    <a style="left:726px">THIS WEEK DEALS</a>
    <a style="left:882px">BRANDS</a>
  </nav>
  <div class="nav-rule"></div>
  <div class="nav-active-bar"></div>
  <div class="side-rule"></div>

  <ul class="category-list">
    <li class="active" style="top:216px">• OPTICS</li>
    <li style="top:259px">• SAFES</li>
    <li style="top:302px">• BIPOD AND TRIPODS</li>
    <li style="top:345px">• LIGHTS</li>
    <li style="top:388px">• CAMERAS</li>
    <li style="top:431px">• TENTS</li>
    <li style="top:473px">• EAR PROTECTION</li>
    <li style="top:516px">• TARGETS</li>
  </ul>

  <main>
    <article class="product-card" style="left:210px;top:214px">
      <div class="product-photo"><div class="shape" role="img" aria-label="Black solar charger case" style="background:radial-gradient(#333,#fff 70%)"></div></div>
      <p class="product-title">Portable Solar Charger Case with Speaker</p>
      <p class="product-price"><s>$89.40</s>$60.78</p>
      <span class="buy-button">Buy Now</span>
    </article>
    <article class="product-card" style="left:578px;top:214px">
      <div class="product-photo"><div class="shape" role="img" aria-label="Pack of batteries" style="background:radial-gradient(#7a7f8a,#fff 70%)"></div></div>
      <p class="product-title">Portable Solar Charger Case with Speaker</p>
      <p class="product-price"><s>$89.40</s>$60.78</p>
      <span class="buy-button">Buy Now</span>
    </article>
    <article class="product-card" style="left:210px;top:404px">
      <div class="product-photo"><div class="shape" role="img" aria-label="Blue ear protection headset" style="background:radial-gradient(#2a5fa8,#fff 70%)"></div></div>
      <p class="product-title">Portable Solar Charger Case with Speaker</p>
      <p class="product-price"><s>$89.40</s>$60.78</p>
      <span class="buy-button">Buy Now</span>
    </article>
    <article class="product-card" style="left:578px;top:404px">
      <div class="product-photo"><div class="shape" role="img" aria-label="Black rifle bipod" style="background:radial-gradient(#3a3a3a,#fff 70%)"></div></div>
      <p class="product-title">Portable Solar Charger Case with Speaker</p>
      <p class="product-price"><s>$89.40</s>$60.78</p>
      <span class="buy-button">Buy Now</span>
    </article>
    <article class="product-card" style="left:210px;top:595px">
      <div class="product-photo"><div class="shape" role="img" aria-label="Coiled bore cleaning rope" style="background:radial-gradient(#3f5a3c,#fff 70%)"></div></div>
      <p class="product-title">Portable Solar Charger Case with Speaker</p>
      <p class="product-price"><s>$89.40</s>$60.78</p>
      <span class="buy-button">Buy Now</span>
    </article>
    <article class="product-card" style="left:578px;top:595px">
      <div class="product-photo"><div class="shape" role="img" aria-label="Small keychain flashlight" style="background:radial-gradient(#2e2e2e,#fff 70%)"></div></div>
      <p class="product-title">Portable Solar Charger Case with Speaker</p>
      <p class="product-price"><s>$89.40</s>$60.78</p>
      <span class="buy-button">Buy Now</span>
    </article>
    <article class="product-card" style="left:210px;top:787px">
      <div class="product-photo"><div class="shape" role="img" aria-label="Dome camping tent" style="background:radial-gradient(#8cb04a,#fff 70%)"></div></div>
      <p class="product-title">Portable Solar Charger Case with Speaker</p>
      <p class="product-price"><s>$89.40</s>$60.78</p>
      <span class="buy-button">Buy Now</span>
    </article>
    <article class="product-card" style="left:578px;top:787px">
      <div class="product-photo"><div class="shape" role="img" aria-label="Red dot rifle sight" style="background:radial-gradient(#c27a1a,#2c2c2c 40%,#fff 70%)"></div></div>
      <p class="product-title">Portable Solar Charger Case with Speaker</p>
      <p class="product-price"><s>$89.40</s>$60.78</p>
      <span class="buy-button">Buy Now</span>
    </article>
  </main>

  <nav class="pagination">
    <span style="left:473px">1</span>
    <span style="left:502px">2</span>
    <span style="left:531px">3</span>
    <span style="left:561px">4</span>
    <span style="left:590px">5</span>
    <span style="left:620px">››</span>
    <span style="left:650px">‹‹</span>
  </nav>

  <footer class="site-footer">
    <p class="footer-links">Home<span class="sep">|</span>About us<span class="sep">|</span>FAQ<span class="sep">|</span>Blog<span class="sep">|</span>Privacy Policy<span class="sep">|</span>Terms &amp; Conditions<span class="sep">|</span>Contact Us<span class="sep">|</span>Shipping and Return</p>
    <p class="copyright">Copyright © 2015 Tallow Brook LLC. All rights reserved</p>
    <p class="helpline">Need Help:(555) 014-2290</p>
    <div class="social"><span></span><span></span><span></span><span></span></div>
  </footer>
</body>
</html>
```